BRAND BOOK design

We are a new swimwear brand. We have a vague idea of what we want. We have some colors we would like to use. We would love someone who can provide simple, sophisticated yet an edgy design for our first brand book. The brand book will contain our campaign photos and you will have to come up with layouts and simple designs to insert these photos and short quotes or descriptions. The brand book will contain our brand identity and express the vibes we want our customers to feel get from our brand.

Target Market(s)

US and Australia

Industry/Entity Type

Fashion

Font styles to use
Other font styles liked:
• Futura Medium

Colors
f9d9e8
cfcfcf
ffffff

Requirements
Must have
• simple modern layout with pop elements.
• photos must be placed with enough space.
• also need minimal space for words.
Nice to have
• Simple layouts that aren't common. Designs that can show our identity.
• Please refer to our website (under construction): www.brightkelphouse.com
Should not have
• mere copies of other brand designs

```html
<!DOCTYPE html>
<html lang="en">
<head>
<meta charset="utf-8">
<title>Brightkelp — Summer 2018</title>
<link rel="stylesheet" href="https://fonts.googleapis.com/css2?family=Josefin+Sans:wght@300&display=swap">
<style>
  :root {
    --blush: #f9d9e8;
    --blush-deep: #f7c6dd;
    --silver: #cfcfcf;
    --white: #ffffff;
    --wall: #5f6f80;
    --wall-dark: #3e4c5c;
    --leaf: #7a9a3a;
  }
  html, body {
    margin: 0;
    padding: 0;
    overflow: hidden;
    background: var(--white);
  }
  .spread {
    position: relative;
    width: 1200px;
    height: 846px;
    overflow: hidden;
    background: var(--white);
    font-family: "Josefin Sans", "Futura", sans-serif;
    font-weight: 300;
    color: var(--white);
  }
  .spread__art {
    position: absolute;
    inset: 0;
  }
  .season-title {
    position: absolute;
    left: 45px;
    top: 44px;
    margin: 0;
    font-size: 46px;
    font-weight: 300;
    letter-spacing: 1px;
    line-height: 1;
  }
  .brand-name {
    position: absolute;
    right: 34px;
    top: 768px;
    margin: 0;
    font-size: 52px;
    font-weight: 300;
    letter-spacing: 3px;
    line-height: 1;
  }
</style>
</head>
<body>
<main class="spread">
  <svg class="spread__art" width="1200" height="846" viewBox="0 0 1200 846" xmlns="http://www.w3.org/2000/svg">
    <defs>
      <linearGradient id="campaign-tones" x1="0" y1="0" x2="0.4" y2="1">
        <stop offset="0" stop-color="var(--leaf)"/>
        <stop offset="0.2" stop-color="var(--wall)"/>
        <stop offset="0.55" stop-color="#d99a7e"/>
        <stop offset="0.8" stop-color="var(--wall-dark)"/>
        <stop offset="1" stop-color="#8a7660"/>
      </linearGradient>
    </defs>

    <rect class="campaign-photo" x="318" y="22" width="570" height="806"
          fill="url(#campaign-tones)" role="img"
          aria-label="Campaign photo: model in a coral strapless cut-out bikini leaning on a concrete wall under lemon trees"/>

    <!-- top corner block -->
    <polygon class="mask" points="0,0 1200,0 1200,22 740,22 22,315 0,330" fill="var(--white)"/>
    <polygon class="corner-block" points="22,22 622,22 22,268" fill="var(--blush-deep)"/>
    <polygon class="corner-stripe" points="695,22 740,22 22,315 22,283" fill="var(--silver)"/>

    <!-- bottom corner stripes -->
    <polygon class="mask" points="470,828 1185,535 1200,535 1200,846 470,846" fill="var(--white)"/>
    <polygon class="corner-stripe" points="470,828 505,828 1185,550 1185,535" fill="var(--blush-deep)"/>
    <polygon class="corner-stripe" points="520,828 540,828 1185,564 1185,555" fill="var(--silver)"/>
    <polygon class="corner-stripe" points="560,828 585,828 1185,582 1185,572" fill="var(--blush-deep)"/>
    <polygon class="corner-stripe" points="600,828 618,828 1185,596 1185,588" fill="var(--silver)"/>
    <polygon class="corner-block" points="660,828 1185,613 1185,828" fill="var(--blush-deep)"/>
  </svg>

  <h1 class="season-title">SUMMER 2018</h1>
  <p class="brand-name">BRIGHTKELP</p>
</main>
</body>
</html>
```